The Maple Arch Dental Offices Double-Sided A5 Flyer Highlighting Strengths & All Locations.

Designs are looking good. I just feel that they're too much in terms of content. Slight change in strategy. I would like a double sided A5 Flyer that has the following:

Front Side:

1. Brand (The Maple Arch Dental Offices). Use the logo that has Dental Offices beneath the words "The Maple Arch."
2. Highlight only the following keywords: Affordable. Friendly. Experienced Dental Care. Kids Friendly. We Accept All Insurance. 0% Interest Payment Plans.
3. Dental Services: Family Dentistry, Teeth Whitening, Braces, Implants, Veneers, Sedation.

Back Side:

This is where I want to highlight how convenient The Maple Arch is. We have 15 locations and growing. So here you can use our tagline:

We're Always Close By! With 15 Locations and Counting.

I want to list all 15 locations with each locations address and unique number. You can find those at https://maplearchsmiles.com/locations
The designer that can provide all locations in a catchy, easy to read and clean design will be selected.

The base of the flyer should utilize a white background. Keep it clean. Keep it fresh.

I'm looking to stand out from all competition with something unique and different. Get creative.

Target Market(s)

Women 30-40 years of age.

Industry/Entity Type

Dental

Font styles to use
Sans Serif

Colors
86cfc6
33b8a4
00a990
f59195
fdfdfb
fdf9cf
dddddd

Requirements
Must have
• Proper brand and color elements. Use white background.
Nice to have
• Surprise me with great ideas and design.
Should not have
• Prices.

```html
<!DOCTYPE html>
<html lang="en">
<head>
<meta charset="utf-8">
<title>The Maple Arch Dental Offices – A5 Flyer</title>
<link rel="stylesheet" href="https://fonts.googleapis.com/css2?family=Open+Sans:wght@300;400;600;700&family=Oswald:wght@600&family=Fredoka:wght@600&display=swap">
<style>
  :root {
    --teal-soft: #86cfc6;
    --teal-mid: #33b8a4;
    --teal-deep: #00a990;
    --pink: #f59195;
    --pink-hot: #ee3f6b;
    --white: #fdfdfb;
    --grey-line: #dddddd;
    --ink: #2f2f31;
    --band: #3a3a3c;
    --black: #111111;
    --stage: #f1efea;
  }
  * { box-sizing: border-box; margin: 0; padding: 0; }
  html, body { width: 1200px; height: 842px; overflow: hidden; }
  body {
    background: var(--stage);
    font-family: "Open Sans", Arial, sans-serif;
    position: relative;
  }
  .flyer-side {
    position: absolute;
    top: 45px;
    width: 530px;
    height: 752px;
    background: var(--white);
    overflow: hidden;
  }
  .flyer-back { left: 50px; }
  .flyer-front { left: 614px; }

  /* ---------- Back side: locations ---------- */
  .family-photo {
    position: absolute; left: 0; top: 0; width: 530px; height: 210px;
    background: linear-gradient(120deg, #f4f1ee 0%, #e9dcd2 35%, #d9bfae 55%, #f2ece7 80%, #ffffff 100%);
  }
  .tagline-band {
    position: absolute; left: 0; top: 210px; width: 530px; height: 56px;
    background: var(--band);
    color: var(--white);
    text-align: center;
    font-weight: 300;
    font-size: 21px;
    letter-spacing: 1.6px;
    line-height: 24px;
    padding-top: 5px;
    text-transform: uppercase;
  }
  .locations-frame {
    position: absolute; left: 0; top: 266px; width: 530px; height: 486px;
    background: var(--teal-mid);
  }
  .locations-grid {
    position: absolute; left: 14px; top: 2px; width: 503px; height: 460px;
    background: var(--white);
    display: grid;
    grid-template-columns: 172px 162px 169px;
    grid-template-rows: repeat(5, 92px);
  }
  .location {
    padding: 10px 6px 0 13px;
    color: var(--ink);
    border-right: 1px solid var(--teal-soft);
    border-bottom: 1px solid var(--teal-soft);
  }
  .location:nth-child(3n) { border-right: none; }
  .location:nth-last-child(-n+3) { border-bottom: none; }
  .location-name {
    color: var(--teal-deep);
    font-weight: 600;
    font-size: 12px;
    line-height: 15px;
    margin-bottom: 4px;
  }
  .location-former {
    font-size: 7.4px;
    line-height: 9px;
    margin-bottom: 3px;
  }
  .location-address, .location-phone {
    font-size: 8.6px;
    line-height: 12.5px;
  }
  .grid-knots {
    position: absolute; left: 14px; top: 2px;
    pointer-events: none;
  }

  /* ---------- Front side: services ---------- */
  .front-shapes { position: absolute; left: 0; top: 0; }
  .corner-note {
    position: absolute; right: 24px; top: 18px;
    color: var(--white);
    font-weight: 700;
    font-size: 31px;
    line-height: 35px;
    text-align: right;
  }
  .kids-badge {
    position: absolute; left: 34px; top: 332px;
    width: 132px; height: 132px; border-radius: 50%;
    background: radial-gradient(circle at 40% 30%, #f7667f 0%, var(--pink-hot) 60%, #e02e5c 100%);
    color: var(--white);
    font-family: "Fredoka", "Comic Sans MS", sans-serif;
    font-weight: 600;
    font-size: 24px;
    line-height: 28px;
    letter-spacing: 1px;
    text-align: center;
    padding-top: 36px;
    text-transform: uppercase;
  }
  .insurance-note {
    position: absolute; left: 23px; top: 476px;
    color: var(--white);
    font-weight: 300;
    font-size: 27px;
    line-height: 32px;
  }
  .payment-note {
    position: absolute; left: 22px; top: 554px;
    color: var(--white);
    font-family: "Oswald", "Arial Narrow", sans-serif;
    font-weight: 600;
    line-height: 1.05;
  }
  .payment-note .payment-lead { display: block; font-size: 36px; }
  .payment-note .payment-tail { display: block; font-size: 29px; }
  .brand-lockup {
    position: absolute; left: 26px; top: 652px;
    display: flex; align-items: center; gap: 10px;
  }
  .brand-dot {
    width: 40px; height: 40px; border-radius: 50%;
    background: var(--teal-soft);
  }
  .brand-name {
    color: #c9c9c9;
    font-weight: 400;
    font-size: 32px;
    line-height: 36px;
  }
  .brand-subline {
    position: absolute; left: 108px; top: 703px;
    color: #9a9a9a;
    font-size: 9.5px;
    letter-spacing: 1.4px;
    text-transform: uppercase;
  }
  .services-title {
    position: absolute; right: 38px; top: 318px;
    color: var(--white);
    font-weight: 400;
    font-size: 49px;
    line-height: 47px;
    text-align: right;
  }
  .services-list {
    position: absolute; right: 24px; top: 432px;
    list-style: none;
    text-align: right;
  }
  .services-list li {
    color: var(--white);
    font-size: 27px;
    line-height: 41px;
    display: flex; align-items: center; justify-content: flex-end; gap: 12px;
  }
  .services-list li::after {
    content: "";
    width: 12px; height: 12px; border-radius: 50%;
    background: var(--pink-hot);
    border: 3px solid var(--white);
  }
</style>
</head>
<body>

<section class="flyer-side flyer-back" aria-label="Back side: locations">
  <div class="family-photo" role="img" aria-label="Photo of a smiling family of four: father, mother and two children"></div>
  <h2 class="tagline-band">We're Always Close By!<br>With 15 Locations and Counting.</h2>
  <div class="locations-frame">
    <div class="locations-grid">
      <article class="location">
        <h3 class="location-name">at Willow Mall</h3>
        <p class="location-address">412 Willow Street<br>Unit W118 (in Willow Mall)<br>Barrie ON, L4N 0A1</p>
        <p class="location-phone">Tel: (705) 555-0142</p>
      </article>
      <article class="location">
        <h3 class="location-name">at Heronfield Plaza</h3>
        <p class="location-address">88 Heronfield Parkway East<br>Unit 204, Heronfield Plaza<br>Brampton ON, L6Z 0A2</p>
        <p class="location-phone">Tel: 647-555-0117</p>
      </article>
      <article class="location">
        <h3 class="location-name">at Ashgrove St.</h3>
        <p class="location-former">Formerly Dr. Ellery &amp; Associates</p>
        <p class="location-address">57 Ashgrove St.<br>Brantford ON, N3R 0B4</p>
        <p class="location-phone">Tel: (519) 555-0186</p>
      </article>

      <article class="location">
        <h3 class="location-name">at Linden St. W.</h3>
        <p class="location-former">Formerly Brightwave Dental – Brantford</p>
        <p class="location-address">210 Linden Street West<br>Unit 3B, Brantford ON, N3T 0C5</p>
        <p class="location-phone">Tel: (519) 555-0163</p>
      </article>
      <article class="location">
        <h3 class="location-name">at Birchwood St. E.</h3>
        <p class="location-former">Formerly Hillside Family Dental</p>
        <p class="location-address">41 Birchwood Street East<br>Unit 6, Dundas, ON L9H 0D7</p>
        <p class="location-phone">Tel: (289) 555-0128</p>
      </article>
      <article class="location">
        <h3 class="location-name">at Cedar Hollow Rd.</h3>
        <p class="location-former">Formerly Cedar Hollow Dental</p>
        <p class="location-address">1840 Cedar Hollow Road<br>Unit 4, Etobicoke ON, M9V 0E2</p>
        <p class="location-phone">Tel: (647) 555-0174</p>
      </article>

      <article class="location">
        <h3 class="location-name">at Northgate College Blvd</h3>
        <p class="location-former">Formerly Brightwave Dental</p>
        <p class="location-address">120 Northgate College Blvd<br>Unit 105, Etobicoke,<br>ON M9V 0F3. Tel: (647) 555-0139</p>
      </article>
      <article class="location">
        <h3 class="location-name">at Pinecrest Rd.</h3>
        <p class="location-former">Formerly Pinecrest Dental</p>
        <p class="location-address">2960 Pinecrest Road, Unit 104,<br>Mississauga, ON L4Y 0G1</p>
        <p class="location-phone">Tel: (647) 555-0151</p>
      </article>
      <article class="location">
        <h3 class="location-name">at Elmview Rd. E.</h3>
        <p class="location-former">Formerly Fairmont Dental</p>
        <p class="location-address">3380 Elmview Road East, Unit 201<br>Mississauga ON, L4T 0H6</p>
        <p class="location-phone">Tel: (647) 555-0195</p>
      </article>

      <article class="location">
        <h3 class="location-name">at Riverbend Mall</h3>
        <p class="location-address">355 Riverbend Rd. E. #118<br>Riverbend Mall (2nd Floor)<br>Mississauga ON, L5A 0J2</p>
        <p class="location-phone">Tel: 647-555-0108</p>
      </article>
      <article class="location">
        <h3 class="location-name">at Fernhill Road</h3>
        <p class="location-address">4870 Fernhill Rd.<br>Unit # 3, Mississauga,<br>Ontario L4W 0K5</p>
        <p class="location-phone">Tel: 647-555-0122</p>
      </article>
      <article class="location">
        <h3 class="location-name">at Lakeshore Plaza</h3>
        <p class="location-former">Formerly Lakeshore Dental</p>
        <p class="location-address">2075 Harbourview Ave. East, Unit 6<br>Scarborough ON, M1R 0L3</p>
        <p class="location-phone">Tel: (647) 555-0147</p>
      </article>

      <article class="location">
        <h3 class="location-name">at Oakridge Square</h3>
        <p class="location-former">Formerly Oakridge Square Dental</p>
        <p class="location-address">4390A Oakridge Road<br>Scarborough ON, M1E 0M8</p>
        <p class="location-phone">Tel: (647) 555-0169</p>
      </article>
      <article class="location">
        <h3 class="location-name">at Hollins Rd.</h3>
        <p class="location-address">1880 Hollins Road, Unit 5<br>Scarborough ON,<br>M1P 0N4</p>
        <p class="location-phone">Tel: (647) 555-0131</p>
      </article>
      <article class="location">
        <h3 class="location-name">at Millvale / Hamilton</h3>
        <p class="location-address">540 Ridgeline Hwy, Unit #2<br>Stoney Creek ON,<br>L8G 0P9</p>
        <p class="location-phone">Tel: 289-555-0183</p>
      </article>
    </div>
    <svg class="grid-knots" width="503" height="460" viewBox="0 0 503 460" aria-hidden="true">
      <g fill="var(--teal-soft)">
        <circle cx="172" cy="92" r="7"/><circle cx="334" cy="92" r="7"/>
        <circle cx="172" cy="184" r="7"/><circle cx="334" cy="184" r="7"/>
        <circle cx="172" cy="276" r="7"/><circle cx="334" cy="276" r="7"/>
        <circle cx="172" cy="368" r="7"/><circle cx="334" cy="368" r="7"/>
      </g>
    </svg>
  </div>
</section>

<section class="flyer-side flyer-front" aria-label="Front side: services">
  <svg class="front-shapes" width="530" height="752" viewBox="0 0 530 752">
    <defs>
      <linearGradient id="photoTone" x1="0" y1="0" x2="1" y2="1">
        <stop offset="0" stop-color="#dfe3e8"/>
        <stop offset="0.35" stop-color="#3f6fc0"/>
        <stop offset="0.55" stop-color="#e6cdb8"/>
        <stop offset="1" stop-color="#f3efea"/>
      </linearGradient>
      <linearGradient id="tealWash" x1="0" y1="0" x2="1" y2="1">
        <stop offset="0" stop-color="#5cc4b6"/>
        <stop offset="0.5" stop-color="#86cfc6"/>
        <stop offset="1" stop-color="#4dbcad"/>
      </linearGradient>
    </defs>
    <polygon points="0,0 308,0 470,186 186,462 0,272" fill="url(#photoTone)" role="img" aria-label="Photo of a smiling young woman reclining in a dental chair"/>
    <polygon points="314,0 530,0 530,280" fill="var(--pink)"/>
    <polygon points="478,184 530,236 530,752 424,752 192,464" fill="url(#tealWash)"/>
    <polygon points="0,280 184,472 410,752 0,752" fill="var(--black)"/>
  </svg>

  <p class="corner-note">Kids<br>Friendly</p>
  <p class="kids-badge">Kids<br>Friendly</p>

  <p class="insurance-note">We Accept<br>All Insurance</p>
  <p class="payment-note"><span class="payment-lead">0% Interest</span><span class="payment-tail">Payment Plans</span></p>

  <div class="brand-lockup">
    <span class="brand-dot" aria-hidden="true"></span>
    <span class="brand-name">The Maple Arch</span>
  </div>
  <p class="brand-subline">Dental Office at Willow Mall</p>

  <h2 class="services-title">Dental<br>Services</h2>
  <ul class="services-list">
    <li>Family Dentistry</li>
    <li>Teeth Whitening</li>
    <li>Braces</li>
    <li>Implants</li>
    <li>Veneers</li>
    <li>Sedation</li>
  </ul>
</section>

</body>
</html>
```